Webdesign für Kosmetikstudio
Zielgruppe
Kosmetikstudio, für gehobene Ansprüche mit speziellen Anwendungen
Zielgruppe: Frauen und Männer von 18-88 (mittleres und gehobenes Einkommen)
Aufgabenstellung
BRIEFING ORDNUNGSGEMÄSS LESEN!!!
- Da die Kundin kein Logo hat, bitte 528417306 von foto.lumeno als Gestaltungselement nutzen ( das runde mit rosa)
daneben soll stehen: Kosmetikstudio Chemnitz Inhaberin Regina Volkert
- das 'Pink' aus der jetzigen Webseite soll beibehalten wrden -> CI (kein Schwarz als Zusatzfarbe, als Schriftfarbe jedoch möglich)
- die Shops: Dr. Pellwitz GmbH und LUC MAVRONE sollen mit ihren Logos als Gestaltungselement eingearbeitet werden
- klare Struktur und Aussage, keine Schnörgel, modern
- Kosmetik soll im Vordergrund stehen, die angegebene Webseite soll NICHT als Grundlage dienen, weil viele Inhalte nicht mehr korrekt sind

```html
<!DOCTYPE html>
<html lang="de">
<head>
<meta charset="utf-8">
<title>Regina Volkert – Kosmetikstudio Chemnitz</title>
<link href="https://fonts.googleapis.com/css2?family=Lato:wght@300;400;700&display=swap" rel="stylesheet">
<style>
:root{
  --pink:#f51fbf;
  --pink-soft:#fdeefa;
  --pink-pale:#fbe3f5;
  --grey-band:#f2f2f2;
  --line:#e3e3e3;
  --text:#2a2a2a;
  --muted:#777;
  --footer:#2b2b2b;
}
*{box-sizing:border-box;margin:0;padding:0}
html,body{width:1200px;height:4375px;overflow:hidden}
body{position:relative;font-family:'Lato',sans-serif;color:var(--text);background:#fff}
.abs{position:absolute}
.btn{position:absolute;display:flex;align-items:center;justify-content:center;border-radius:20px;font-size:9px;font-weight:700;letter-spacing:.3px;text-transform:uppercase}
.btn-fill{background:var(--pink);color:#fff}
.btn-line{border:1.5px solid var(--pink);color:var(--pink);background:#fff}
h2.section-title{position:absolute;font-weight:400;font-size:25px;line-height:31px;letter-spacing:.5px;text-transform:uppercase;color:var(--text)}
.copy{position:absolute;font-size:11px;line-height:18px;color:#555}

/* top bar & header */
.topbar{top:0;left:0;width:1200px;height:17px;background:var(--pink);color:#fff;font-size:8.5px}
.topbar .addr{position:absolute;left:775px;top:3px;display:flex;align-items:center;gap:4px}
.topbar .contact{position:absolute;right:76px;top:3px;font-weight:700}
.header{top:17px;left:0;width:1200px;height:58px;background:#fff}
.brand{position:absolute;left:75px;top:5px;display:flex;align-items:center;gap:8px}
.brand-circle{width:52px;height:52px;border-radius:50%;border:1.5px solid #c9c9c9}
.brand-name{font-size:11px;line-height:12px;color:var(--text)}
.brand-name small{display:block;font-size:7px;color:var(--muted)}
.nav{position:absolute;left:357px;top:22px;display:flex;gap:30px;font-size:10px;color:var(--text)}

/* hero */
.hero-media{top:75px;left:0;width:1200px;height:499px;background:linear-gradient(100deg,#e6e3e2 0%,#f4efee 30%,#c9a391 58%,#8a5a45 72%,#efeeee 90%)}
.hero-title{position:absolute;left:243px;top:249px;font-size:44px;font-weight:300;letter-spacing:1px;color:#333}
.hero-text{left:243px;top:310px;width:410px;font-size:11px;line-height:18px;color:#333}
.dots{position:absolute;left:567px;top:549px;display:flex;gap:12px;align-items:center}
.dots span{width:5px;height:5px;border-radius:50%;background:#fff}
.dots span.on{width:24px;border-radius:3px;background:var(--pink)}

/* microneedling */
.benefit{position:absolute;left:630px;width:325px;height:88px;border:1px solid var(--line);background:#fff;display:flex;align-items:center;padding-left:10px;gap:22px;font-size:12px;line-height:17px}
.benefit .ico{width:66px;height:66px;border-radius:50%;background:var(--pink-soft);display:flex;align-items:center;justify-content:center;flex:none}

/* service cards */
.grey-band{left:0;top:1128px;width:1200px;height:377px;background:var(--grey-band)}
.service-card{position:absolute;top:1011px;width:325px;height:406px;background:#fff}
.service-card .media{height:211px}
.service-card h3{position:absolute;left:21px;top:245px;font-weight:400;font-size:18px;line-height:24px;text-transform:uppercase}
.service-card .mark{position:absolute;left:-3px;top:248px;width:3px;height:38px;background:var(--pink)}
.service-card p{position:absolute;left:21px;width:285px;font-size:10.5px;line-height:18px;color:#555}
.service-card .more{position:absolute;left:21px;font-size:9px;font-weight:700;color:var(--pink);display:flex;align-items:center;gap:8px}

/* treatments */
.treat{position:absolute;left:243px;width:712px;border:1px solid #ddd;background:#fff}
.treat .name{position:absolute;left:18px;font-size:10.5px;line-height:14px;color:var(--pink)}
.treat .desc{position:absolute;left:183px;width:420px;font-size:10.5px;line-height:18px;color:#444}
.treat .price{position:absolute;right:20px;width:60px;text-align:center;color:var(--pink);font-size:15px;line-height:18px}
.treat .price small{display:block;font-size:8px;color:#aaa;line-height:10px}

/* tiles */
.pink-band{left:0;top:2355px;width:1200px;height:313px;background:var(--pink-soft)}
.tile{position:absolute;top:2400px;width:164px;height:224px;background:#fff}
.tile .media{height:146px}
.tile .label{position:absolute;left:0;right:0;top:158px;text-align:center;font-size:10.5px;line-height:17px;text-transform:uppercase;color:var(--text)}
.tile .bar{position:absolute;left:72px;top:212px;width:20px;height:3px;background:var(--pink)}

/* partners */
.partner-band{left:0;top:2670px;width:1200px;height:130px;background:var(--grey-band)}
.partner{position:absolute;top:2720px;font-size:15px;letter-spacing:1px;color:#555}

/* pricing */
.plan{position:absolute;top:2936px;width:225px;height:563px;border:1px solid #ddd;background:#fff}
.plan .badge{position:absolute;left:61px;top:-48px;width:102px;height:102px;border-radius:50%;background:var(--pink-pale);display:flex;align-items:center;justify-content:center}
.plan .badge span{width:84px;height:84px;border-radius:50%;background:#fff;display:flex;align-items:center;justify-content:center}
.plan .kicker{position:absolute;top:74px;width:100%;text-align:center;font-size:9px;color:#aaa;letter-spacing:.5px}
.plan .title{position:absolute;top:90px;width:100%;text-align:center;font-size:24px;font-weight:400;color:var(--pink)}
.plan ul{position:absolute;left:18px;top:150px;list-style:none;width:190px}
.plan li{position:relative;padding-left:20px;font-size:10px;line-height:12.5px;color:#555;margin-bottom:12.5px}
.plan li::before{content:"";position:absolute;left:0;top:4px;width:4px;height:4px;border-radius:50%;background:var(--pink)}
.plan .price{position:absolute;top:418px;width:100%;text-align:center;font-size:40px;font-weight:300;color:var(--pink)}
.plan .dur{position:absolute;top:472px;width:100%;text-align:center;font-size:9px;color:#bbb}

/* foot care */
.foot-band{left:0;top:3649px;width:1200px;height:285px;background:var(--pink-soft)}
/* location */
.loc-band{left:0;top:3946px;width:1200px;height:370px;background:#f7f7f7}
.loc-card{left:631px;top:4070px;width:324px;height:142px;background:#fff}
.footer{left:0;top:4316px;width:1200px;height:59px;background:var(--footer);color:#ddd;font-size:8.5px}
</style>
</head>
<body>

<div class="abs topbar">
  <div class="addr">
    <svg width="8" height="10" viewBox="0 0 8 10"><path d="M4 0a4 4 0 0 0-4 4c0 3 4 6 4 6s4-3 4-6a4 4 0 0 0-4-4zm0 5.5A1.5 1.5 0 1 1 4 2.5a1.5 1.5 0 0 1 0 3z" fill="#fff"/></svg>
    Chemnitz, Lindenauer Str. 48 &nbsp; T:0173/ 514 62 07
  </div>
  <div class="contact">KONTAKTIEREN SIE UNS</div>
</div>

<header class="abs header">
  <div class="brand">
    <div class="brand-circle"></div>
    <div class="brand-name">REGINA VOLKERT<small>KOSMETIKSTUDIO CHEMNITZ INHABERIN</small></div>
  </div>
  <nav class="nav">
    <span>Informationen</span><span>Fusspflege</span><span>MicroNeedling</span><span>Ernährungs- und Gesundheitsberatung</span><span>Medi-taping</span><span>Kontakt</span>
  </nav>
  <div class="btn btn-line" style="left:967px;top:14px;width:156px;height:29px;font-weight:400">Termin online anfragem</div>
</header>

<section>
  <div class="abs hero-media" role="img" aria-label="Foto: Kosmetikerin behandelt das Gesicht einer Kundin mit einem Microneedling-Gerät"></div>
  <h1 class="hero-title">MICRONEEDLING</h1>
  <p class="copy hero-text">Die sanfte Methode ist eine nicht- invasive Technik zur kurzzeitigen Öffnung der epidermalen Hautbarriere, damit hochwirksame kosmetische Substanzen optimal in die Haut eindringen können.</p>
  <div class="btn btn-fill" style="left:243px;top:399px;width:119px;height:26px">Mehr Erfahrung</div>
  <div class="dots"><span class="on"></span><span></span><span></span><span></span></div>
</section>

<section>
  <h2 class="section-title" style="left:243px;top:657px">Microneedling - Die<br>Anti- Aging Revolution</h2>
  <p class="copy" style="left:243px;top:744px;width:330px">Es handelt sich beim MicroNeedling um eine sehr angenehme Medical-Beauty Behandlung, welche die Faltentiefe verringert und die Hauttextur verbessert. Durch die gleichmäßige schonende Perforationsmethode wird beim MicroNeedling der hauteigene Regenerationsprozess und die Microzirkulation aktiviert, die körpereigene Kollagen- und Elastinbildung stimuliert.</p>
  <div class="benefit" style="top:662px">
    <div class="ico"><svg width="28" height="28" viewBox="0 0 28 28"><path d="M14 4c-4 6-7 9-7 13a7 7 0 0 0 14 0c0-4-3-7-7-13z" fill="none" stroke="#f51fbf" stroke-width="1.5"/></svg></div>
    <div>verbesserte Wirkstoffaufnahme und dadurch verstärktem Effekt der gewählten Behandlungsprodukte</div>
  </div>
  <div class="benefit" style="top:764px">
    <div class="ico"><svg width="28" height="28" viewBox="0 0 28 28"><circle cx="14" cy="14" r="9" fill="none" stroke="#f51fbf" stroke-width="1.5"/><path d="M9 14h10M14 9v10" stroke="#f51fbf" stroke-width="1.5"/></svg></div>
    <div>Glättungsintensität von Falten<br>Steigerung des Zellstoffwechsels</div>
  </div>
  <div class="btn btn-fill" style="left:519px;top:898px;width:158px;height:27px">Termin online anfragen</div>
</section>

<section>
  <div class="abs grey-band"></div>
  <article class="service-card" style="left:243px">
    <div class="media" role="img" aria-label="Foto: Notizbuch, Äpfel, Nüsse und Maßband auf weißem Holztisch" style="background:linear-gradient(120deg,#d9c2a4,#f3f1ee 45%,#e7e4df 70%,#c96b4a)"></div>
    <span class="mark"></span>
    <h3>Ernährungs- und<br>Gesundheitsberatung</h3>
    <p style="top:308px">Hier erlernen Sie die Grundlagen zur Ernährung und Gesundheit für Ihr bewusstes Leben.</p>
    <div class="more" style="top:360px">MENR INFO <svg width="16" height="10" viewBox="0 0 16 10"><path d="M0 5h14M10 1l4 4-4 4" fill="none" stroke="#f51fbf" stroke-width="1.5"/></svg></div>
  </article>
  <article class="service-card" style="left:631px">
    <div class="media" role="img" aria-label="Foto: Frau erhält eine Rückenbehandlung" style="background:linear-gradient(120deg,#c9a08a,#e9d3c5 50%,#f2ebe7)"></div>
    <span class="mark"></span>
    <h3>Medi-taping</h3>
    <p style="top:282px">Bleiben Sie fit, beweglich und schmerzfrei im Alltag und beim Sport. Medi-taping kann Sie hier, auch bei Schmerzen, unterstützen.</p>
    <div class="more" style="top:356px">MENR INFO <svg width="16" height="10" viewBox="0 0 16 10"><path d="M0 5h14M10 1l4 4-4 4" fill="none" stroke="#f51fbf" stroke-width="1.5"/></svg></div>
  </article>
</section>

<section>
  <h2 class="section-title" style="left:243px;top:1586px">Exklusivbehandlungen</h2>
  <div class="treat" style="top:1649px;height:79px">
    <div class="name" style="top:31px">Frischzellenkur</div>
    <div class="desc" style="top:22px">Reinigungspeeling, Tiefenreinigung,Einschleusen von hauttypgerechten Wirkstoffkonzentraten mit Ultraschall,Maske, Abschlusspflege</div>
    <div class="price" style="top:22px">80 €<small>ca.60 Min.</small></div>
  </div>
  <div class="treat" style="top:1739px;height:97px">
    <div class="name" style="top:31px">Traitement Prestige</div>
    <div class="desc" style="top:22px">Faltenkorrigierendes und feuchtigkeitsspendendes Behandlungsarrangement mit einer innovativen Wirkstoffkombination gegen vorzeitige Alterungserscheinungen der Haut.</div>
    <div class="price" style="top:22px">72 €<small>90 Min.</small></div>
  </div>
  <div class="treat" style="top:1850px;height:78px">
    <div class="name" style="top:31px">Traitement Caviar</div>
    <div class="desc" style="top:22px">Neue Elastizität und Spannkraft für die Haut durch luxuriösen Kaviarextrakt und reines Meerquellwasser.</div>
    <div class="price" style="top:22px">80 €<small>ca.60 Min.</small></div>
  </div>
  <div class="treat" style="top:1941px;height:79px">
    <div class="name" style="top:31px">Traitement Renovia</div>
    <div class="desc" style="top:22px">Systempflege zur effektiven Behandlung von unerwünschten Mimikfalten mit „Filler – Like“ Wirkstoffen und einem Extrakt aus Apfelstammzellen.</div>
    <div class="price" style="top:22px">72 €<small>ca.60 Min.</small></div>
  </div>
  <div class="treat" style="top:2033px;height:78px">
    <div class="name" style="top:31px">Traitement VELAMED</div>
    <div class="desc" style="top:22px">Intensive Behandlung mit einem neuen Fruchtsäurekomplex AHA-Plus Repairwirkstoffen zur Festigung der Haut für eine verbesserte Elastizität</div>
    <div class="price" style="top:22px">72 €<small>90 Min.</small></div>
  </div>
  <div class="treat" style="top:2125px;height:78px">
    <div class="name" style="top:26px">Traitement Multi- Lift<br>Anti - Age</div>
    <div class="desc" style="top:19px">Intensive Behandlung mit einem neuen Fruchtsäurekomplex AHA-Plus Repairwirkstoffen zur Festigung der Haut für eine verbesserte Elastizität</div>
    <div class="price" style="top:22px">72 €<small>ca.60 Min.</small></div>
  </div>
  <div class="btn btn-fill" style="left:519px;top:2240px;width:158px;height:27px">Termin online anfragen</div>
</section>

<section>
  <div class="abs pink-band"></div>
  <div class="tile" style="left:243px"><div class="media" role="img" aria-label="Foto: Ganzkörpermassage" style="background:linear-gradient(135deg,#b88b74,#e9d6cb 60%,#f4f1ef)"></div><div class="label">Kokostraum-Ganz<br>Körpermassage</div><span class="bar"></span></div>
  <div class="tile" style="left:426px"><div class="media" role="img" aria-label="Foto: Frau zwischen rosa Blüten" style="background:linear-gradient(135deg,#efd9ee,#f7f0f6 50%,#d9b9c9)"></div><div class="label" style="top:167px">Methode Aphrodite</div><span class="bar"></span></div>
  <div class="tile" style="left:608px"><div class="media" role="img" aria-label="Foto: Kundin mit Gesichtsmaske bei der Anti-Aging-Behandlung" style="background:linear-gradient(135deg,#7c5a48,#d8c3b6 55%,#eeeae7)"></div><div class="label">Anti-Aging-Behandlu<br>ngen</div><span class="bar"></span></div>
  <div class="tile" style="left:791px"><div class="media" role="img" aria-label="Foto: Nahaufnahme gepflegter Haut" style="background:linear-gradient(135deg,#f3e6e2,#e8cfc6 60%,#f7f1ef)"></div><div class="label">Korrektur von<br>Mimikfalten</div><span class="bar"></span></div>
</section>

<section>
  <div class="abs partner-band"></div>
  <h2 class="section-title" style="left:241px;top:2703px">Unsere Partners -<br>die Shops:</h2>
  <div class="partner" style="left:680px">LUC MAVRONE</div>
  <div class="partner" style="left:835px">PELLWITZ</div>
</section>

<section>
  <div class="plan" style="left:243px">
    <div class="badge"><span><svg width="46" height="40" viewBox="0 0 46 40"><path d="M23 37S3 25 3 12A10 10 0 0 1 23 8a10 10 0 0 1 20 4c0 13-20 25-20 25z" fill="none" stroke="#f51fbf" stroke-width="2.5"/></svg></span></div>
    <div class="kicker">KOSMETIK</div><div class="title">CLASSIC</div>
    <ul><li>Reinigung</li><li>Augenbrauenkorrektur</li><li>Tiefenreinigung z. B. Peeling</li><li>Entfernen von Unreinheiten</li><li>hauttypgerechte Wirkstoffkonzentrate</li><li>Pflegemaske</li><li>Abschlusspflege</li></ul>
    <div class="price">45 €</div><div class="dur">30 MIN.</div>
    <div class="btn btn-line" style="left:34px;top:499px;width:157px;height:27px">Termin online anfragem</div>
  </div>
  <div class="plan" style="left:487px">
    <div class="badge"><span><svg width="46" height="44" viewBox="0 0 46 44"><path d="M23 3l6 13 14 2-10 10 3 14-13-7-13 7 3-14L3 18l14-2z" fill="none" stroke="#f51fbf" stroke-width="2.5" stroke-linejoin="round"/></svg></span></div>
    <div class="kicker">GESICHTSBEHANDLUNGEN</div><div class="title">BASIC</div>
    <ul><li>neutrale Hautreinigung</li><li>Hautdiagnose</li><li>Korrigieren der Augenbrauen</li><li>Tiefenreinigung z. B. Peeling</li><li>Entfernen von Unreinheiten</li><li>hauttypgerechte Wirkstoffkonzentrate</li><li>Gesichts-, Dekolleté- und Nackenmassage</li><li>Pflegemaske</li><li>Abschlusspflege</li></ul>
    <div class="price">35 €</div><div class="dur">30 MIN.</div>
    <div class="btn btn-line" style="left:34px;top:499px;width:157px;height:27px">Termin online anfragem</div>
  </div>
  <div class="plan" style="left:730px">
    <div class="badge"><span><svg width="50" height="40" viewBox="0 0 50 40"><path d="M5 12l10 10 10-16 10 16 10-10-4 22H9z" fill="none" stroke="#f51fbf" stroke-width="2.5" stroke-linejoin="round"/><path d="M9 38h32" stroke="#f51fbf" stroke-width="2.5"/></svg></span></div>
    <div class="kicker">KOSMETIK</div><div class="title">PREMIUM</div>
    <ul><li>Reinigung</li><li>Tiefenreinigung</li><li>Entfernen von Unreinheiten</li><li>All in One</li><li>hauttypgerechte Wirkstoffkonzentrate</li><li>Gesichts- und Dekolletémassage</li><li>Pflegemaske</li><li>Abschlusspflege</li></ul>
    <div class="price">65 €</div><div class="dur">90 MIN.</div>
    <div class="btn btn-line" style="left:34px;top:499px;width:157px;height:27px">Termin online anfragem</div>
  </div>
  <div class="btn btn-fill" style="left:487px;top:3538px;width:225px;height:28px">Kosmetik im Studio Chemnitz</div>
</section>

<section>
  <div class="abs foot-band"></div>
  <h2 class="section-title" style="left:241px;top:3725px">Fusspflege</h2>
  <p class="copy" style="left:243px;top:3776px;width:450px;font-size:10.5px">Befreien Sie Ihre Füße von Schwielen, Hühneraugen, Hornhaut oder Pilzen! Sie gewinnen eine bessere Mobilität und steigern Ihr gesamtes Wohlbefinden!</p>
  <div class="btn btn-fill" style="left:245px;top:3844px;width:156px;height:26px">Kontaktieren Sie uns</div>
  <div class="abs" role="img" aria-label="Video: medizinische Fußpflege im Behandlungsraum" style="left:730px;top:3718px;width:225px;height:160px;background:linear-gradient(135deg,#c9d3e6,#e9ecf2 50%,#b9c2d2)">
    <svg class="abs" style="left:84px;top:51px" width="58" height="58" viewBox="0 0 58 58"><circle cx="29" cy="29" r="27" fill="none" stroke="#fff" stroke-width="3"/><path d="M23 18l17 11-17 11z" fill="#fff"/></svg>
  </div>
</section>

<section>
  <div class="abs loc-band"></div>
  <div class="abs" role="img" aria-label="Foto: Wartebereich des Studios mit Korbsesseln und Tulpen" style="left:243px;top:4005px;width:325px;height:241px;background:linear-gradient(135deg,#e8e4dc,#c9a38a 45%,#8a5b42 70%,#d9d2c8)"></div>
  <h2 class="section-title" style="left:633px;top:4025px">Sie finden mich</h2>
  <div class="abs loc-card">
    <span class="abs" style="left:0;top:26px;width:3px;height:20px;background:var(--pink)"></span>
    <div class="abs" style="left:53px;top:26px;font-size:11px;color:var(--pink)">Kosmetikstudio Chemnitz</div>
    <div class="abs" style="left:53px;top:50px;font-size:11px;line-height:17px;color:var(--text)">Lindenauer Str. 48<br>09116 Chemnitz<br>T: 0173/ 514 62 07</div>
  </div>
</section>

<footer class="abs footer">
  <div class="abs" style="left:75px;top:25px">Besucher: &nbsp; &nbsp; 16666</div>
  <div class="abs" style="left:196px;top:25px">Impressum</div>
  <div class="abs" style="right:76px;top:25px">© 2020 Alle Rechte vorbehalten</div>
</footer>

</body>
</html>
```